letterhead package
corin maddox agency
Use same font as used in my logo
any fonts
Professional
Corin Maddox Agency
President
5172 Birchley Rd
Oceanside NY 11619
info@cmvopr.com
www.cmvopr.com
-national and international horse transportation-
Logo File AI version

```html
<!DOCTYPE html>
<html lang="en">
<head>
<meta charset="utf-8">
<title>Corin Maddox Agency — Business Cards</title>
<link href="https://fonts.googleapis.com/css2?family=Open+Sans:wght@400;600;700&display=swap" rel="stylesheet">
<style>
  :root {
    --bg: #ece6dc;
    --card: #1d1b1a;
    --card-edge: #2a2726;
    --gold: #d2a730;
    --gold-light: #f1d46a;
    --gold-dark: #9c7418;
    --silver: #e4e4e4;
    --text: #f2f2f2;
    --muted: #cfcfcf;
  }
  * { box-sizing: border-box; margin: 0; padding: 0; }
  html, body { width: 1200px; height: 852px; overflow: hidden; }
  body {
    background: var(--bg);
    font-family: "Open Sans", Arial, sans-serif;
    position: relative;
  }
  .card {
    position: absolute;
    width: 540px;
    height: 310px;
    border-radius: 16px;
    overflow: hidden;
    background: linear-gradient(160deg, var(--card-edge), var(--card) 60%);
    color: var(--text);
    box-shadow: 0 10px 24px rgba(0,0,0,0.25);
  }
  .card--front { left: 50px; top: 90px; }
  .card--back { left: 610px; top: 452px; }
  .swoosh { position: absolute; left: 0; bottom: 0; width: 540px; height: 310px; }

  .brand {
    display: flex; flex-direction: column; align-items: center; gap: 10px;
    color: var(--gold); font-weight: 700; letter-spacing: 1.5px; text-align: center;
  }
  .brand__mark { width: 38px; height: 38px; background: var(--gold); border-radius: 50%; }
  .brand__name { font-size: 19px; line-height: 1.25; text-transform: uppercase; }

  .divider { position: absolute; width: 1px; background: #8a8a8a; }

  .identity__name { color: var(--gold); font-weight: 700; font-size: 15px; }
  .identity__role { font-size: 11px; color: var(--muted); margin-top: 3px; }
  .identity__address { font-size: 11px; line-height: 1.55; margin-top: 16px; }

  .contacts { list-style: none; font-size: 11px; line-height: 1; }
  .contacts li { display: flex; align-items: center; gap: 7px; height: 16px; }
  .contacts svg { width: 10px; height: 10px; fill: var(--gold); flex: none; }

  /* front */
  .card--front .brand { position: absolute; left: 34px; top: 88px; width: 200px; }
  .card--front .divider { left: 262px; top: 26px; height: 200px; }
  .card--front .identity { position: absolute; left: 278px; top: 26px; }
  .card--front .contacts { position: absolute; left: 278px; top: 136px; }

  /* back */
  .card--back .brand { position: absolute; left: 170px; top: 24px; width: 200px; }
  .card--back .brand__name { font-size: 17px; }
  .card--back .divider { left: 270px; top: 134px; height: 96px; }
  .card--back .identity { position: absolute; left: 50px; top: 146px; width: 204px; text-align: right; }
  .card--back .identity__address { margin-top: 12px; }
  .card--back .contacts { position: absolute; left: 286px; top: 138px; }
</style>
</head>
<body>

<svg width="0" height="0" style="position:absolute">
  <defs>
    <linearGradient id="goldBand" x1="0" y1="0" x2="1" y2="0">
      <stop offset="0" stop-color="#9c7418"/>
      <stop offset="0.35" stop-color="#f1d46a"/>
      <stop offset="0.65" stop-color="#c9981f"/>
      <stop offset="1" stop-color="#f0d067"/>
    </linearGradient>
    <symbol id="i-phone" viewBox="0 0 10 10"><path d="M2 0.5 L3.6 2.4 L2.8 3.6 C3.5 5 5 6.5 6.4 7.2 L7.6 6.4 L9.5 8 L8.3 9.5 C4.5 9.2 0.8 5.5 0.5 1.7 Z"/></symbol>
    <symbol id="i-mobile" viewBox="0 0 10 10"><path d="M3 0 H7 A1 1 0 0 1 8 1 V9 A1 1 0 0 1 7 10 H3 A1 1 0 0 1 2 9 V1 A1 1 0 0 1 3 0 Z M3 1.5 V7.5 H7 V1.5 Z"/></symbol>
    <symbol id="i-fax" viewBox="0 0 10 10"><path d="M2.5 0 H7.5 V3 H9 A1 1 0 0 1 10 4 V8 H8 V10 H2 V8 H0 V4 A1 1 0 0 1 1 3 H2.5 Z M3 6 V9 H7 V6 Z"/></symbol>
    <symbol id="i-mail" viewBox="0 0 10 10"><path d="M0 2 H10 V8 H0 Z M0.8 2.6 L5 5.6 L9.2 2.6 Z" fill-rule="evenodd"/></symbol>
    <symbol id="i-web" viewBox="0 0 10 10"><circle cx="5" cy="5" r="5"/></symbol>
  </defs>
</svg>

<article class="card card--front">
  <svg class="swoosh" viewBox="0 0 540 310" aria-hidden="true">
    <path d="M0 250 C160 214 350 290 540 212 L540 226 C350 300 160 232 0 264 Z" fill="var(--silver)"/>
    <path d="M0 266 C160 234 350 302 540 228 L540 310 L0 310 Z" fill="url(#goldBand)"/>
  </svg>
  <div class="brand">
    <span class="brand__mark"></span>
    <span class="brand__name">Corin Maddox<br>Agency</span>
  </div>
  <span class="divider"></span>
  <div class="identity">
    <p class="identity__name">Corin Maddox Agency</p>
    <p class="identity__role">President</p>
    <p class="identity__address">5172 Birchley Rd<br>Oceanside NY 11619</p>
  </div>
  <ul class="contacts">
    <li><svg><use href="#i-phone"/></svg>555 204 7318</li>
    <li><svg><use href="#i-mobile"/></svg>555 731 4062</li>
    <li><svg><use href="#i-fax"/></svg>555 204 7390</li>
    <li><svg><use href="#i-mail"/></svg>info@cmvopr.com</li>
    <li><svg><use href="#i-web"/></svg>www.cmvopr.com</li>
  </ul>
</article>

<article class="card card--back">
  <svg class="swoosh" viewBox="0 0 540 310" aria-hidden="true">
    <path d="M0 250 C160 214 350 290 540 212 L540 226 C350 300 160 232 0 264 Z" fill="var(--silver)"/>
    <path d="M0 266 C160 234 350 302 540 228 L540 310 L0 310 Z" fill="url(#goldBand)"/>
  </svg>
  <div class="brand">
    <span class="brand__mark"></span>
    <span class="brand__name">Corin Maddox<br>Agency</span>
  </div>
  <span class="divider"></span>
  <div class="identity">
    <p class="identity__name">Corin Maddox Agency</p>
    <p class="identity__role">President</p>
    <p class="identity__address">5172 Birchley Rd<br>Oceanside NY 11619</p>
  </div>
  <ul class="contacts">
    <li><svg><use href="#i-phone"/></svg>555 204 7318</li>
    <li><svg><use href="#i-mobile"/></svg>555 731 4062</li>
    <li><svg><use href="#i-fax"/></svg>555 204 7390</li>
    <li><svg><use href="#i-mail"/></svg>info@cmvopr.com</li>
    <li><svg><use href="#i-web"/></svg>www.cmvopr.com</li>
  </ul>
</article>

</body>
</html>
```